Bellwether Home Inspections

We need stationery for our new home inspection company. We inspect homes for people prior to purchasing to ensure the property is in good condition, as well as inspecting new homes to ensure they have been built to the appropriate standards. We are happy to look at combinations of colours. The use of a water mark would be good. Open to suggestions.

Industry/Entity Type

Home Inspection

```html
<!DOCTYPE html>
<html lang="en">
<head>
<meta charset="utf-8">
<title>Bellwether Home Inspections — Stationery</title>
<link rel="stylesheet" href="https://fonts.googleapis.com/css2?family=Questrial&family=Libre+Baskerville:wght@400;700&display=swap">
<style>
  :root {
    --backdrop: #e4e4e4;
    --orange-core: #fbc51c;
    --orange-mid: #f7a614;
    --orange-edge: #ef8209;
    --brand-blue: #1f4f7d;
    --ink: #3c3c3c;
    --muted: #6b6b6b;
    --paper: #ffffff;
    --tab: #2d3a4a;
  }
  html, body { margin: 0; padding: 0; overflow: hidden; }
  body { width: 1200px; height: 705px; background: var(--backdrop); position: relative; font-family: "Questrial", sans-serif; }
  .piece { position: absolute; box-shadow: 0 2px 6px rgba(0,0,0,.18); }
  .orange {
    background: radial-gradient(ellipse at 45% 35%, var(--orange-core) 0%, var(--orange-mid) 45%, var(--orange-edge) 100%);
    color: var(--paper);
  }
  .wordmark { font-family: "Questrial", sans-serif; font-weight: 400; text-align: center; line-height: 1.05; }
  .wordmark .mark-square { display: block; margin: 0 auto 10px; background: currentColor; }

  /* folder */
  .folder { left: 30px; top: 150px; width: 300px; height: 360px; display: flex; align-items: center; justify-content: center; }
  .folder .wordmark { font-size: 24px; }
  .folder .mark-square { width: 34px; height: 34px; }

  /* envelope back */
  .envelope { left: 428px; top: 88px; width: 332px; height: 182px; overflow: hidden; }
  .envelope svg { position: absolute; inset: 0; }

  /* card front */
  .card-front { left: 428px; top: 290px; width: 332px; height: 183px; display: flex; align-items: center; justify-content: center; }
  .card-front .wordmark { font-size: 19px; }
  .card-front .mark-square { width: 40px; height: 40px; margin-bottom: 14px; }

  /* business cards */
  .biz { top: 490px; width: 188px; height: 120px; }
  .biz-white { left: 362px; background: var(--paper); display: flex; align-items: center; padding: 0 10px; box-sizing: border-box; gap: 10px; }
  .biz-white .wordmark { color: var(--brand-blue); font-size: 10px; width: 80px; }
  .biz-white .mark-square { width: 18px; height: 18px; margin-bottom: 6px; }
  .biz-details { font-size: 5px; color: var(--muted); flex: 1; }
  .biz-name { color: var(--brand-blue); font-size: 8.5px; letter-spacing: .3px; }
  .biz-role { font-size: 4.5px; letter-spacing: 1px; margin-bottom: 6px; }
  .biz-row { display: flex; align-items: center; gap: 4px; margin: 2px 0; padding-bottom: 2px; border-bottom: 0.5px solid #ddd; }
  .biz-row svg { width: 5px; height: 5px; fill: var(--muted); }
  .biz-address { margin-top: 4px; }
  .biz-orange { left: 563px; display: flex; align-items: center; justify-content: center; }
  .biz-orange .wordmark { font-size: 10px; }
  .biz-orange .mark-square { width: 20px; height: 20px; margin-bottom: 8px; }

  /* letterhead */
  .letterhead { left: 780px; top: 86px; width: 368px; height: 520px; background: var(--paper); font-family: "Libre Baskerville", serif; color: var(--ink); }
  .lh-brand { position: absolute; left: 22px; top: 22px; display: flex; align-items: center; gap: 14px; color: var(--brand-blue); }
  .lh-brand .brand-square { width: 70px; height: 70px; background: currentColor; }
  .lh-brand .brand-name { font-family: "Questrial", sans-serif; font-size: 19px; line-height: 1.05; margin-top: 28px; }
  .lh-meta { position: absolute; right: 254px; top: 128px; text-align: right; font-size: 5px; line-height: 1.55; }
  .lh-meta .label { font-variant: small-caps; font-weight: 700; font-size: 6px; }
  .lh-meta .block { margin-bottom: 8px; }
  .lh-body { position: absolute; left: 129px; top: 128px; width: 218px; font-size: 5.2px; line-height: 1.75; }
  .lh-body p { margin: 0 0 9px; }
  .lh-body p.gap { margin-top: 22px; }
  .lh-sign { margin-top: 22px; }
  .lh-sign .name { font-variant: small-caps; font-weight: 700; font-size: 6px; }
  .lh-footer { position: absolute; left: 22px; bottom: 18px; border-left: 1.5px solid var(--brand-blue); padding-left: 10px; font-size: 5px; line-height: 1.7; }
</style>
</head>
<body>

<section class="piece orange folder" aria-label="Presentation folder">
  <div class="wordmark"><span class="mark-square"></span>Bellwether<br>Home Inspections</div>
</section>

<section class="piece orange envelope" aria-label="Envelope back">
  <svg viewBox="0 0 332 182" width="332" height="182">
    <polyline points="0,20 166,52 332,20" fill="none" stroke="rgba(180,90,0,.35)" stroke-width="1"/>
    <rect x="164" y="38" width="18" height="28" rx="3" fill="var(--tab)"/>
  </svg>
</section>

<section class="piece orange card-front" aria-label="Card front">
  <div class="wordmark"><span class="mark-square"></span>Bellwether<br>Home Inspections</div>
</section>

<section class="piece biz biz-white" aria-label="Business card front">
  <div class="wordmark"><span class="mark-square"></span>Bellwether<br>Home Inspections</div>
  <div class="biz-details">
    <div class="biz-name">MARLON VERITY</div>
    <div class="biz-role">OWNER</div>
    <div class="biz-row"><svg viewBox="0 0 10 10"><path d="M2 0h2l1 3-1.5 1a6 6 0 0 0 2.5 2.5L7 5l3 1v2a2 2 0 0 1-2 2A8 8 0 0 1 0 2a2 2 0 0 1 2-2z"/></svg>(555) 240 7718</div>
    <div class="biz-row"><svg viewBox="0 0 10 10"><path d="M0 2h10v6H0z M0 2l5 4 5-4" stroke="#6b6b6b" fill="none"/></svg>marlon@bellwether.example</div>
    <div class="biz-row"><svg viewBox="0 0 10 10"><circle cx="5" cy="5" r="4.5"/></svg>www.bellwether.example</div>
    <div class="biz-address">14 Orchard Lane, Unit 5</div>
  </div>
</section>

<section class="piece orange biz biz-orange" aria-label="Business card back">
  <div class="wordmark"><span class="mark-square"></span>Bellwether<br>Home Inspections</div>
</section>

<section class="piece letterhead" aria-label="Letterhead">
  <header class="lh-brand">
    <span class="brand-square"></span>
    <span class="brand-name">Bellwether<br>Home Inspections</span>
  </header>
  <aside class="lh-meta">
    <div class="block"><div class="label">Date</div>08 . 15 . 2015</div>
    <div class="block"><div class="label">Address</div>48 Linden Row,<br>City Name, Country Name</div>
  </aside>
  <article class="lh-body">
    <p>Lorem ipsum dolor sit amet, consectetur adipisicing elit,</p>
    <p>Sed do eiusmod tempor incididunt ut labore et dolore magna aliqua. Ut enim ad minim veniam, quis nostrud exercitation ullamco laboris nisi ut aliquip ex ea commodo consequat.</p>
    <p>Duis aute irure dolor in reprehenderit in voluptate velit esse cillum dolore eu fugiat nulla pariatur. Excepteur sint occaecat cupidatat non proident, sunt in culpa qui officia deserunt mollit anim id est laborum.</p>
    <p>Sed ut perspiciatis unde omnis iste natus error sit voluptatem accusantium doloremque laudantium, totam rem aperiam, eaque ipsa quae ab illo inventore veritatis et quasi architecto beatae vitae dicta sunt explicabo.</p>
    <p class="gap">Nemo enim ipsam voluptatem quia voluptas sit aspernatur aut odit aut fugit, sed quia consequuntur magni dolores eos qui ratione voluptatem sequi nesciunt. Neque porro quisquam est, qui dolorem ipsum quia dolor sit amet, consectetur, adipisci velit, sed quia non numquam eius modi tempora incidunt ut labore et dolore magnam aliquam quaerat voluptatem.</p>
    <div class="lh-sign"><div class="name">Ellis Hartwell</div>graphic designer and ceo.</div>
  </article>
  <footer class="lh-footer">
    48 Linden Row, / City Name, Country Name<br>
    t. 55 (01) 204 318XX<br>
    e. hello@bellwether.example
  </footer>
</section>

</body>
</html>
```